Need Letterhead Design & Matching Business Card

I have a logo that I love already. But the letterhead is less than appealing and boring. I'd like a design for my letterhead which I will match with business cards. Also, I'd like to have used fonts that are generally available, as my current letterhead uses a font named "SPACE" which nobody has unless they download it...so when a Word version is forwarded, it looks awful on the receiver's screed due to not having the font. That being said, modern is the look we like and are going for.

My business is "Halloran Brightmoor PC" - a law firm specializing in representing people who have suffered catastrophic injuries or death (plane, auto, train crashes etc.).

See attached letterhead, which has all of the pertinent information. My logo is also attached in various formats.

```html
<!DOCTYPE html>
<html lang="en">
<head>
<meta charset="utf-8">
<title>Halloran Brightmoor PC — Stationery</title>
<link href="https://fonts.googleapis.com/css2?family=Inter:wght@400;600;700&family=Arimo:wght@400;700&display=swap" rel="stylesheet">
<style>
:root{
  --bg:#dddbe6;
  --paper:#ffffff;
  --ink:#000000;
  --text:#555555;
  --text-dark:#222222;
  --rule:#666666;
  --flap-line:#d6d6d6;
  --panel-grey:#c6c4cf;
  --panel-mark:#dedce6;
  --signature:#cfcfcf;
}
*{margin:0;padding:0;box-sizing:border-box}
html,body{width:1200px;height:1097px;overflow:hidden}
body{background:var(--bg);position:relative;font-family:"Inter",Arial,sans-serif;color:var(--text)}

.sheet{position:absolute;background:var(--paper);box-shadow:0 10px 24px rgba(60,55,80,.18)}

/* Letterhead */
.letterhead{left:80px;top:173px;width:477px;height:618px}
.brand-square{position:absolute;background:var(--ink);display:flex;align-items:center;justify-content:center;text-align:center;color:var(--paper);font-family:"Inter",Arial,sans-serif;font-weight:600;letter-spacing:.06em;text-transform:uppercase;line-height:1.35}
.letterhead .brand-square{left:0;top:0;width:88px;height:87px;font-size:8px;padding:0 8px}
.sender{position:absolute;left:104px;top:29px;font-size:8.3px;line-height:12px}
.sender-name{color:var(--ink);font-weight:700}
.header-rule{position:absolute;top:25px;width:1px;height:45px;background:var(--rule)}
.header-rule.first{left:194px}
.header-rule.second{left:306px}
.address{position:absolute;left:205px;top:28px;font-size:8.2px;line-height:14.2px}
.contacts{position:absolute;left:316px;top:27px;font-size:8.2px;line-height:15px;list-style:none}
.contacts li{display:flex;align-items:center;gap:6px}
.contacts svg{width:8px;height:8px;fill:none;stroke:#555;stroke-width:1.2}

.letter{position:absolute;left:45px;top:131px;width:386px;font-family:"Arimo",Arial,sans-serif;font-size:7.9px;line-height:12.5px;color:var(--text)}
.letter-date{margin-left:0}
.recipient{margin:12px 0 0 1px}
.subject{margin:14px 0 0 1px;font-weight:700}
.salutation{margin:14px 0 0}
.letter p.body{margin:7px 0 0 1px}
.letter p.body + p.body{margin-top:20px}
.closing{margin-top:34px}
.signature{margin:4px 0 0 -6px;width:74px;height:36px;background:linear-gradient(90deg,var(--signature),#ececec);border-radius:2px}

.letter-footer .brand-square{left:0;top:568px;width:46px;height:50px;position:absolute}
.footer-name{position:absolute;left:52px;top:578px;font-family:"Inter",Arial,sans-serif;font-size:10.3px;line-height:16px;color:var(--ink);text-transform:uppercase}
.footer-bar{position:absolute;left:0;bottom:0;width:100%;height:4px;background:var(--ink)}

/* Envelope front */
.envelope-front{left:595px;top:173px;width:537px;height:235px}
.envelope-front .brand-square{left:0;top:0;width:66px;height:64px;font-size:6.2px;padding:0 5px}
.return-address{position:absolute;left:76px;top:15px;font-size:8.3px;line-height:12px}

/* Envelope back */
.envelope-back{left:595px;top:452px;width:537px;height:235px}
.envelope-back .flap{position:absolute;left:0;top:0;width:537px;height:70px}
.envelope-back .brand-square{left:249px;top:14px;width:39px;height:39px}

/* Corner panel */
.corner-panel{position:absolute;left:918px;top:815px;width:282px;height:282px;background:var(--panel-grey);display:flex;align-items:center;justify-content:center;text-align:center;font-family:"Inter",Arial,sans-serif;font-weight:600;font-size:24px;line-height:1.3;letter-spacing:.06em;text-transform:uppercase;color:var(--panel-mark)}
</style>
</head>
<body>

<section class="sheet letterhead">
  <div class="brand-square">Halloran Brightmoor PC</div>

  <div class="sender">
    <div class="sender-name">M. Dorian Castell, Esq</div>
    <div class="sender-title">President</div>
  </div>
  <span class="header-rule first"></span>
  <address class="address" style="font-style:normal">
    4820 Larkspur Ave.<br>suite 600 ,Westbrook,<br>CA 90417
  </address>
  <span class="header-rule second"></span>
  <ul class="contacts">
    <li><svg viewBox="0 0 10 10"><path d="M2 1 L4 1 L5 3.5 L3.8 4.5 Q5 6.3 5.6 6.2 L6.5 5 L9 6 L9 8 Q8 9.2 6 8.6 Q2 7 1 3 Q1 1.6 2 1Z"/></svg>(855) 555-0142</li>
    <li><svg viewBox="0 0 10 10"><rect x="1" y="2" width="8" height="6"/><path d="M1 2 L5 5.5 L9 2"/></svg>dorian@halloranbrightmoor.com</li>
    <li><svg viewBox="0 0 10 10"><circle cx="5" cy="5" r="4"/><ellipse cx="5" cy="5" rx="1.8" ry="4"/><path d="M1 5 H9"/></svg>www.halloranbrightmoor.com</li>
  </ul>

  <article class="letter">
    <div class="letter-date">March 15, 2024</div>
    <div class="recipient">Northvale Health<br>48 Fenwick Mill Road</div>
    <div class="subject">Sub: How to change our business policy</div>
    <div class="salutation">Dear Mr. Hale,</div>
    <p class="body">We welcome you as shareholders of Northvale Health Incorporated (NASDAQ : NVLH). We are pleased to inform you that on September 1, 2009, Veridant, Inc. (“Veridant”) merged with a subsidiary of Northvale Health Incorporated (“Northvale Health”). As a result of the merger, each share of Veridant preferred healthcare Common Stock, if any.</p>
    <p class="body">Please note that the method of delivery is at your option and risk. If you send these documents by mail, we strongly recommend that you use registered mail, properly insured, with return receipt requested Incorporated (“Northvale Health”). As a result of the merger.</p>
    <p class="body">We are pleased to have you as a stockholder of Northvale Health and look forward to enjoying your continued support of the combined company.</p>
    <div class="closing">Sincerely yours,</div>
    <div class="signature" role="img" aria-label="Handwritten signature of the sender"></div>
  </article>

  <footer class="letter-footer">
    <div class="brand-square"></div>
    <div class="footer-name">Halloran<br>Brightmoor PC</div>
    <div class="footer-bar"></div>
  </footer>
</section>

<section class="sheet envelope-front">
  <div class="brand-square">Halloran Brightmoor PC</div>
  <address class="return-address" style="font-style:normal">
    4820 Larkspur Ave.<br>suite 600 ,Westbrook,<br>CA 90417
  </address>
</section>

<section class="sheet envelope-back">
  <svg class="flap" viewBox="0 0 537 70" aria-hidden="true">
    <path d="M0.5 0 V28 Q0.5 69 42 69 H495 Q536.5 69 536.5 28 V0" fill="none" stroke="#d6d6d6" stroke-width="1"/>
  </svg>
  <div class="brand-square"></div>
</section>

<div class="corner-panel">Halloran<br>Brightmoor PC</div>

</body>
</html>
```